I need a business card to launch my business. I am a carpenter who works with wood and metal framing. I do commercial and residential properties. I do the final fixtures in expensive residential properties. For example custom made wardrobes, prefinished doors and skirtings. I have an eye for detail and take pride in my work.

I don't want to be pigeon holed as a guy with a tool belt and a hammer. I want to look like a professional company. I want my logo to be modern and young and edgy. I don't have any preference for colours but don't want yellow.

Industry/Entity Type

Residential

Contact Information for Business Card

Oakridge Joinery
specialising in residential and commercial fit outs

Mark Dawson
Phone: 0417 352 068
oakridgejoinery@mailbox-example.com

Logo styles of interest
Pictorial/Combination Logo
Wordmark Logo
Lettermark Logo

```html
<!DOCTYPE html>
<html lang="en">
<head>
<meta charset="utf-8">
<title>Oakridge Joinery – Business Card</title>
<link rel="stylesheet" href="https://fonts.googleapis.com/css2?family=Roboto+Slab:wght@400;600&display=swap">
<style>
  :root {
    --stage: #2a2a2a;
    --card: #050505;
    --gold: #d4a441;
    --white: #f2f2f2;
    --grey: #bdbdbd;
  }
  * { margin: 0; padding: 0; box-sizing: border-box; }
  html, body {
    width: 1200px;
    height: 900px;
    overflow: hidden;
    background: var(--stage);
    font-family: "Roboto Slab", Georgia, serif;
  }
  .stage {
    width: 1200px;
    height: 900px;
    display: flex;
    align-items: center;
    justify-content: center;
    gap: 60px;
  }
  .card {
    width: 520px;
    height: 318px;
    background: var(--card);
    position: relative;
    box-shadow: 0 10px 30px rgba(0,0,0,0.5);
  }
  .brand {
    display: flex;
    align-items: center;
    gap: 12px;
    color: var(--white);
    font-weight: 600;
    letter-spacing: 0.04em;
    white-space: nowrap;
  }
  .brand-square {
    width: 14px;
    height: 14px;
    background: var(--gold);
    flex: none;
  }
  /* Front */
  .card-front .brand {
    position: absolute;
    left: 0;
    right: 0;
    top: 110px;
    justify-content: center;
    font-size: 38px;
  }
  .card-front .brand-square { width: 22px; height: 22px; }
  .tagline {
    position: absolute;
    left: 0;
    right: 0;
    top: 186px;
    text-align: center;
    color: var(--white);
    font-size: 16px;
    line-height: 1.35;
  }
  .tagline .accent { color: var(--gold); }
  /* Back */
  .card-back .brand {
    position: absolute;
    right: 40px;
    top: 150px;
    font-size: 22px;
  }
  .contact {
    position: absolute;
    right: 40px;
    top: 196px;
    text-align: right;
    font-size: 13px;
    line-height: 1.5;
    color: var(--white);
  }
  .contact-name {
    color: var(--gold);
    font-size: 17px;
    letter-spacing: 0.03em;
    margin-bottom: 2px;
  }
  .contact-label, .contact-email-user { color: var(--gold); }
  .contact-sep { color: var(--grey); }
</style>
</head>
<body>
  <main class="stage">
    <section class="card card-front" aria-label="Card front">
      <div class="brand">
        <span class="brand-square" aria-hidden="true"></span>
        <span class="brand-name">OAKRIDGE JOINERY</span>
      </div>
      <p class="tagline">
        specialising in<br>
        <span class="accent">residential</span> and <span class="accent">commercial</span> fit outs
      </p>
    </section>

    <section class="card card-back" aria-label="Card back">
      <div class="brand">
        <span class="brand-square" aria-hidden="true"></span>
        <span class="brand-name">OAKRIDGE JOINERY</span>
      </div>
      <div class="contact">
        <p class="contact-name">MARK DAWSON</p>
        <p class="contact-line">
          <span class="contact-label">P:</span> 0417 352 068 <span class="contact-sep">//</span>
          <span class="contact-email-user">mark</span>@oakridgejoinery-example.com.au
        </p>
        <p class="contact-web">www.oakridgejoinery-example.com.au</p>
      </div>
    </section>
  </main>
</body>
</html>
```